Velvet Harbor (A luxury Travel Website)

website text attached in document below

images also attached

feel free to use other images if needed

Target Market(s)

Luxury Seekers and wealthy couples / families

Industry/Entity Type

Luxury Travel

Coding

Coded - Design and coding required

Number of Pages Required

1 page

Requirements
Must have
• A luxury design and easy use.
Nice to have
• Ease of use of page, incorporation of images into the flow of the site

```html
<!DOCTYPE html>
<html lang="en">
<head>
<meta charset="utf-8">
<title>Velvet Harbor — Luxury Travel</title>
<link href="https://fonts.googleapis.com/css2?family=Poppins:wght@400;500;600;700&family=Prata&display=swap" rel="stylesheet">
<style>
:root{
  --green:#1db56e;
  --green-dark:#14b866;
  --cyan:#19c2ef;
  --ink:#1c1c1c;
  --muted:#333;
  --white:#fff;
  --vision-bg:#8fdcb8;
  --mission-bg:#aee9f5;
  --sand:#efece6;
}
*{box-sizing:border-box;margin:0;padding:0}
html,body{width:1200px;height:5172px;overflow:hidden}
body{position:relative;background:var(--white);font-family:"Poppins",sans-serif;color:var(--ink)}
.abs{position:absolute}
.serif{font-family:"Prata",serif}

/* header */
.site-header{left:0;top:0;width:1200px;height:60px;background:var(--white)}
.brand{left:45px;top:12px;font-family:"Poppins",sans-serif;font-size:24px;font-weight:500;color:#6a9fc2;letter-spacing:1px}
.nav{top:20px;left:0;width:1200px;font-size:12px;font-weight:500;color:#222}
.nav span{position:absolute}
.btn-book{left:1015px;top:8px;width:113px;height:34px;background:var(--green);color:#fff;font-size:13px;display:flex;align-items:center;justify-content:center}

/* hero */
.hero{left:0;top:60px;width:1200px;height:630px;background:linear-gradient(180deg,#5f8fa0 0%,#3f7187 45%,#2d5e78 70%,#e9eef2 100%)}
.hero-title{left:70px;top:190px;color:#fff;font-weight:700;font-size:50px;line-height:68px;letter-spacing:2px}
.hero-sub{left:70px;top:340px;color:#fff;font-size:28px;letter-spacing:1px}
.btn-learn{left:70px;top:390px;width:145px;height:42px;background:var(--cyan);color:#fff;font-size:13px;display:flex;align-items:center;justify-content:center}
.btn-outline{left:228px;top:390px;width:146px;height:42px;border:2px solid #fff;color:#fff;font-size:13px;display:flex;align-items:center;justify-content:center}

.search-bar{left:140px;top:672px;width:918px;height:63px;background:#fff;border:2px solid #222;box-shadow:0 6px 14px rgba(0,0,0,.25);display:flex;align-items:center;font-size:13px}
.search-loc{width:280px;height:100%;background:var(--green);color:#fff;display:flex;align-items:center;gap:16px;padding-left:14px}
.search-cell{height:100%;display:flex;align-items:center;gap:12px;padding-left:20px;border-right:1px solid #ddd;color:#333}

/* about */
.about-kicker{left:0;top:830px;width:1200px;text-align:center;color:var(--green);font-size:27px}
.about-title{left:0;top:862px;width:1200px;text-align:center;font-size:44px}
.underline{height:3px;background:var(--green)}
.about-text{left:150px;top:942px;width:900px;text-align:center;font-size:14.5px;line-height:21px;color:var(--muted)}

.vision-section{left:0;top:1060px;width:1200px;height:490px;background:linear-gradient(180deg,#fff 0%,var(--sand) 55%,#d9d2c6 100%)}
.couple-photo{left:720px;top:1040px;width:370px;height:510px;background:linear-gradient(180deg,#e9e4da,#c9bfb2);border-radius:8px}
.value-card{top:1150px;width:248px;height:296px;padding:26px 16px}
.value-card h3{font-family:"Prata",serif;font-weight:400;font-size:24px;margin:14px 0 18px}
.value-card p{font-family:"Prata",serif;font-size:12.5px;line-height:19px;color:#333}
.vision{left:90px;background:var(--vision-bg);border:4px solid var(--green)}
.mission{left:350px;background:var(--mission-bg);border:4px solid var(--cyan)}

/* activities */
.act-title{left:132px;top:1612px;font-size:44px}
.act-text{left:132px;top:1698px;width:640px;font-size:14.5px;line-height:21px;color:var(--muted)}
.act-card{top:1834px;width:238px}
.act-photo{height:188px}
.act-card p{font-family:"Prata",serif;font-size:11px;line-height:17px;color:#333;margin-top:20px;height:100px}
.act-card h4{font-size:18px;font-weight:600;margin-top:18px}

/* adventure */
.adventure{left:0;top:2290px;width:1200px;height:510px;background:linear-gradient(180deg,#7d8c9a 0%,#a99a6a 30%,#7e9a4e 55%,#e8eaed 80%,#fff 100%)}
.adv-title{left:0;top:2360px;width:1200px;text-align:center;color:#fff;font-weight:700;font-size:40px;line-height:56px;letter-spacing:2px}
.btn-adv{left:544px;top:2496px;width:110px;height:38px;background:var(--cyan);color:#fff;font-size:13px;display:flex;align-items:center;justify-content:center}

/* destinations */
.dest-title{left:0;top:2896px;width:1200px;text-align:center;font-size:44px}
.dest{border-radius:8px;box-shadow:0 4px 10px rgba(0,0,0,.2)}

/* newsletter */
.newsletter{left:0;top:3850px;width:1200px;height:570px;background:linear-gradient(180deg,#fff 0%,#c9c8c4 12%,#3b3a3a 38%,#2b3a4d 60%,#6a6f78 85%,#fff 100%)}
.news-title{left:0;top:4110px;width:1200px;text-align:center;color:#fff;font-weight:700;font-size:28px;line-height:40px;letter-spacing:1.5px}
.news-form{left:434px;top:4198px;width:330px;height:36px;background:#fff;border-radius:18px;overflow:hidden;display:flex;align-items:center}
.news-form span{flex:1;padding-left:24px;font-size:12px;color:#999}
.news-form b{width:102px;height:100%;background:var(--green);color:#fff;font-weight:500;font-size:12px;border-radius:18px;display:flex;align-items:center;justify-content:center}

/* testimonials */
.happy-title{left:0;top:4478px;width:1200px;text-align:center;font-size:44px}
.happy-text{left:155px;top:4578px;width:890px;text-align:center;font-family:"Prata",serif;font-size:15px;line-height:21px;color:#222}
.happy-name{left:0;top:4684px;width:1200px;text-align:center;font-size:15px;font-weight:600}
.dots{left:556px;top:4724px;display:flex;gap:8px}
.dots i{width:11px;height:11px;border-radius:50%;background:var(--green);display:block}

/* footer */
.site-footer{left:0;top:4838px;width:1200px;height:334px;background:var(--green-dark);color:#fff}
.footer-brand{left:0;top:4880px;width:1200px;text-align:center;font-size:48px;font-weight:500;letter-spacing:3px;color:#fff}
.footer-text{left:200px;top:4972px;width:800px;text-align:center;font-size:12px;line-height:22px;color:#fff}
.socials{left:520px;top:5024px;display:flex;gap:18px}
.socials i{width:24px;height:24px;background:#fff;border-radius:4px;display:block}
.footer-nav{top:5088px;left:0;width:1200px;font-size:15px;color:#fff}
.footer-nav span{position:absolute}
.footer-rule{left:110px;top:5132px;width:980px;height:1px;background:rgba(255,255,255,.8)}
.copyright{left:0;top:5152px;width:1200px;text-align:center;font-size:11px;color:#fff}
</style>
</head>
<body>

<header class="abs site-header">
  <div class="abs brand">Velvet Harbor</div>
  <nav class="abs nav">
    <span style="left:314px">HOME</span>
    <span style="left:402px">ABOUT</span>
    <span style="left:496px">VACATION PACKAGES</span>
    <span style="left:686px">DEPARTURE</span>
    <span style="left:810px">GIFT CARDS</span>
  </nav>
  <div class="abs btn-book">Book now</div>
</header>

<section class="abs hero" role="img" aria-label="Photo of a couple walking hand in hand on a beach toward the sea, with an airplane swoosh and clouds"></section>
<h1 class="abs hero-title">VACATION HOME FOR<br>THE WHOLE FAMILY</h1>
<p class="abs hero-sub">THE WHOLE WORLD AWAITS.</p>
<div class="abs btn-learn">Learn More</div>
<div class="abs btn-outline">Booking Now</div>

<div class="abs search-bar">
  <div class="search-loc">
    <svg width="22" height="22" viewBox="0 0 24 24"><path d="M3 11 21 3 13 21 11 13Z" fill="#fff"/></svg>
    Search location
  </div>
  <div class="search-cell" style="width:190px">
    <svg width="16" height="16" viewBox="0 0 16 16"><rect x="1" y="3" width="14" height="12" fill="none" stroke="#555" stroke-width="1.4"/><path d="M1 6h14M4 1v3M12 1v3" stroke="#555" stroke-width="1.4"/></svg>
    Thu, Sep 10 <span style="color:#777">&lt; &gt;</span>
  </div>
  <div class="search-cell" style="width:190px">
    <svg width="16" height="16" viewBox="0 0 16 16"><rect x="1" y="3" width="14" height="12" fill="none" stroke="#555" stroke-width="1.4"/><path d="M1 6h14M4 1v3M12 1v3" stroke="#555" stroke-width="1.4"/></svg>
    Fri, Oct 12 <span style="color:#777">&lt; &gt;</span>
  </div>
  <div class="search-cell" style="width:130px">
    <svg width="18" height="16" viewBox="0 0 18 16"><path d="M1 14V4M17 14V9H1M4 9V6h6v3" fill="none" stroke="#555" stroke-width="1.4"/></svg>
    1 <span style="color:#777">&lt; &gt;</span>
  </div>
  <div class="search-cell" style="border:none;width:120px">
    <svg width="16" height="16" viewBox="0 0 16 16"><circle cx="8" cy="5" r="3.5" fill="none" stroke="#555" stroke-width="1.4"/><path d="M2 15c0-4 12-4 12 0" fill="none" stroke="#555" stroke-width="1.4"/></svg>
    1 <span style="margin-left:24px;color:#777">&#8964;</span>
  </div>
</div>

<p class="abs about-kicker">About us</p>
<h2 class="abs serif about-title" style="font-weight:400">What we are?</h2>
<div class="abs underline" style="left:546px;top:918px;width:170px"></div>
<p class="abs serif about-text">Lorem ipsum dolor sit amet consectetur. In sed cras massa in vitae elementum. Accumsan magna praesent vitae ultricies sed. Quis sed lorem sit tempor lacus eget et. Consectetur tincidunt aliquet mauris dictum purus viverra et sagittis non. Nibh varius maecenas sodales nisi ut aliquam nibh. Aliquam commodo ultricies arcu fringilla dolor.</p>

<section class="abs vision-section" role="img" aria-label="Sandy beach background"></section>
<div class="abs couple-photo" role="img" aria-label="Photo of a bride and groom walking barefoot on the sand"></div>

<article class="abs value-card vision">
  <svg width="64" height="64" viewBox="0 0 64 64" fill="none" stroke="#111" stroke-width="2.5"><path d="M4 32C14 18 50 18 60 32 50 46 14 46 4 32Z"/><circle cx="32" cy="32" r="9"/><circle cx="32" cy="32" r="3" fill="#111"/><path d="M32 6v6M14 10l4 5M50 10l-4 5M32 52v6M14 54l4-5M50 54l-4-5"/></svg>
  <h3>Our Vission</h3>
  <p>Lorem ipsum dolor sit amet consectetur. In sed cras massa in vitae elementum. Accumsan magna praesent vitae ultricies sed. Quis sed lorem sit tempor lacus eget et.</p>
</article>
<article class="abs value-card mission">
  <svg width="64" height="64" viewBox="0 0 64 64" fill="none" stroke="#111" stroke-width="2.5"><circle cx="30" cy="34" r="24"/><circle cx="30" cy="34" r="15"/><circle cx="30" cy="34" r="6"/><path d="M30 34 54 10M48 6v10h10"/></svg>
  <h3>Our Mission</h3>
  <p>Lorem ipsum dolor sit amet consectetur. In sed cras massa in vitae elementum. Accumsan magna praesent vitae ultricies sed. Quis sed lorem sit tempor lacus eget et.</p>
</article>

<h2 class="abs serif act-title" style="font-weight:400">Activites</h2>
<div class="abs underline" style="left:132px;top:1670px;width:168px"></div>
<p class="abs serif act-text">Lorem ipsum dolor sit amet consectetur. In sed cras massa in vitae elementum. Accumsan magna praesent vitae ultricies sed. Quis sed lorem sit tempor lacus eget et. Consectetur tincidunt aliquet mauris dictum purus viverra et sagittis non. Nibh varius maecenas sodales nisi ut aliquam nibh. Aliquam commodo ultricies arcu fringilla dolor.</p>

<article class="abs act-card" style="left:104px">
  <div class="act-photo" role="img" aria-label="Photo of the Sydney harbour opera house under a blue sky" style="background:linear-gradient(180deg,#2a78c6,#6fb0e0 60%,#2f5f8a)"></div>
  <p>Lorem ipsum dolor sit amet consectetur. In sed cras massa in vitae elementum. Accumsan magna praesent vitae ultricies sed. Quis sed lorem sit tempor lacus eget et. Consectetur tincidunt aliquet</p>
  <h4>Australia</h4>
</article>
<article class="abs act-card" style="left:372px">
  <div class="act-photo" role="img" aria-label="Photo of a domed mosque skyline over the water in Istanbul" style="background:linear-gradient(180deg,#dfe4e8,#b9b6ad 60%,#6d7b80)"></div>
  <p>Lorem ipsum dolor sit amet consectetur. In sed cras massa in vitae elementum. Accumsan magna praesent vitae ultricies sed. Quis sed lorem sit tempor lacus eget et. Consectetur tincidunt aliquet</p>
  <h4>Turkey</h4>
</article>
<article class="abs act-card" style="left:642px">
  <div class="act-photo" role="img" aria-label="Aerial night photo of the Manhattan skyline" style="background:linear-gradient(180deg,#1b2452,#3a3f7a 50%,#c9913e)"></div>
  <p>Lorem ipsum dolor sit amet consectetur. In sed cras massa in vitae elementum. Accumsan magna praesent vitae ultricies sed. Quis sed lorem sit tempor lacus eget et. Consectetur tincidunt aliquet</p>
  <h4>New York</h4>
</article>
<article class="abs act-card" style="left:912px">
  <div class="act-photo" role="img" aria-label="Photo of the Statue of Liberty at sunset" style="background:linear-gradient(180deg,#5a6a9a,#c99480 55%,#6b5a66)"></div>
  <p>Lorem ipsum dolor sit amet consectetur. In sed cras massa in vitae elementum. Accumsan magna praesent vitae ultricies sed. Quis sed lorem sit tempor lacus eget et. Consectetur tincidunt aliquet</p>
  <h4>New York</h4>
</article>

<section class="abs adventure" role="img" aria-label="Photo of green rolling hills and forest above clouds, with a passenger jet flying toward the viewer"></section>
<h2 class="abs adv-title">ARE YOU READY FOR<br>YOU ADVENTURE</h2>
<div class="abs btn-adv">Book Now</div>

<h2 class="abs serif dest-title" style="font-weight:400">Top Destination</h2>
<div class="abs underline" style="left:526px;top:2952px;width:234px"></div>

<div class="abs dest" style="left:62px;top:3020px;width:333px;height:220px;background:linear-gradient(180deg,#1d2738,#3a3d4a 60%,#b0552e)" role="img" aria-label="Night photo of a city skyline with light trails"></div>
<div class="abs dest" style="left:432px;top:3020px;width:333px;height:220px;background:linear-gradient(180deg,#5f8c3c,#8ab35a 55%,#b7a98a)" role="img" aria-label="Photo of two cyclists riding on a forest trail"></div>
<div class="abs dest" style="left:803px;top:3020px;width:333px;height:220px;background:linear-gradient(180deg,#4b8fd6,#9cc6ec 45%,#d9cbb0)" role="img" aria-label="Photo of a baroque domed church in Vienna"></div>
<div class="abs dest" style="left:64px;top:3270px;width:338px;height:460px;background:linear-gradient(180deg,#7aa6d8,#2e4a86 50%,#8aa0b4)" role="img" aria-label="Photo of a father holding his young child by the sea"></div>
<div class="abs dest" style="left:432px;top:3264px;width:336px;height:220px;background:linear-gradient(180deg,#48627a,#2c3e52 60%,#b9b0a4)" role="img" aria-label="Photo of a couple sitting on the deck of a boat"></div>
<div class="abs dest" style="left:800px;top:3264px;width:336px;height:220px;background:linear-gradient(180deg,#0f5a6e,#3f8c94 45%,#2d4a56)" role="img" aria-label="Photo of a lakeside village below mountains"></div>
<div class="abs dest" style="left:432px;top:3510px;width:336px;height:220px;background:linear-gradient(180deg,#5d86ad,#cfd8e2 55%,#8ea4b8)" role="img" aria-label="Photo of a family steering a sailing boat"></div>
<div class="abs dest" style="left:800px;top:3510px;width:336px;height:220px;background:linear-gradient(180deg,#5a8fd0,#c9d5e0 40%,#6e7f4e)" role="img" aria-label="Photo of snowy mountains above a green valley"></div>

<section class="abs newsletter" role="img" aria-label="Evening photo of a resort pool with cabanas, framed by soft clouds"></section>
<h2 class="abs news-title">SUBCRIBE OUR NEWSLETTER<br>AND GET 10 % OFF</h2>
<div class="abs news-form"><span>Enter your email</span><b>Subscribe</b></div>

<h2 class="abs serif happy-title" style="font-weight:400">Happy Customers</h2>
<p class="abs happy-text">Lorem ipsum dolor sit amet, consectetur adipiscing elit. Leo, non odio turpis mi posuere vel volutpat. Ultrices sit habitant neque faucibus lorem in enim scelerisque in. Suscipit nibh nec eu enim, egestas nullam eu et, habitasse. Sed diam phasellus ultrices id lacus maecenas id sem. Elementum sed eget mattis convallis condimentum suscipit turpis donec ultrices. Non ornare aliquam, nunc libero, ultrices bibendum viverra facilisi.</p>
<p class="abs happy-name">Mira</p>
<div class="abs dots"><i></i><i></i><i></i><i></i><i></i></div>

<footer class="abs site-footer"></footer>
<div class="abs footer-brand">Velvet Harbor</div>
<p class="abs footer-text">lorem ipsum dolor sit amet, consectetur adipiscing elit. sit egestas tristique varius est nullam. sed amet felis, id diam rutrum.<br>justo senectus sed nam orci, puru lorem ipsum dolor sit of to in amet, consectetur adipiscing elit.</p>
<div class="abs socials"><i></i><i></i><i></i><i></i></div>
<nav class="abs footer-nav">
  <span style="left:294px">Home</span>
  <span style="left:394px">About</span>
  <span style="left:496px">Vacation Packages</span>
  <span style="left:696px">Departure</span>
  <span style="left:830px">Give Card</span>
</nav>
<div class="abs footer-rule"></div>
<p class="abs copyright">Copyright 2022 Northwind Travels All Rights Reserved</p>

</body>
</html>
```